Real Estate Website

I am looking for a website design for a website that will be featuring real estate listings across Australia. It will be a website for a real estate agency that operates through all states in Australia.

We like the designs of https://www.brightvaleliving.com.au/ and https://velomira.asia/

On the lifestyle website, we like the sell, buy, sold tabs but would also like lease, and agents. We also need a button somewhere for 'Join Agent Horvex' and 'Login'

On the Velomira site it has a concierge section and we want something like that on the home page.

The contact details to show in the footer are:

Shop 2147B
Level 1 Coralgate Plaza Shopping Centre
87 Tidewell Crescent
Southport

Attached are various versions of the logo and some intro text to go on the home page.

```html
<!DOCTYPE html>
<html lang="en">
<head>
<meta charset="utf-8">
<title>Agent Horvex — Real Estate Across Australia</title>
<link href="https://fonts.googleapis.com/css2?family=Poppins:wght@300;400;500;600;700;800&display=swap" rel="stylesheet">
<style>
:root{
  --gold:#a8730a;
  --gold-light:#d19d16;
  --gold-dark:#7a4e08;
  --ink:#1c1f3a;
  --text:#3c3c46;
  --muted:#6b6b75;
  --cream:#f5f2ec;
  --line:#d8d3c8;
  --white:#ffffff;
  --dark:#1d2230;
}
*{box-sizing:border-box;margin:0;padding:0}
html,body{width:1200px;height:5296px;overflow:hidden}
body{font-family:'Poppins',sans-serif;color:var(--text);background:var(--white);position:relative}
.abs{position:absolute}
.btn-gold{position:absolute;display:flex;align-items:center;justify-content:center;background:linear-gradient(180deg,var(--gold-light),var(--gold-dark));color:#fff;font-weight:600;font-size:13px;letter-spacing:.5px;text-transform:uppercase;border-radius:3px}
.btn-outline{position:absolute;display:flex;align-items:center;justify-content:center;border:1.5px solid rgba(255,255,255,.85);color:#fff;font-weight:600;font-size:13px;letter-spacing:.5px;text-transform:uppercase;border-radius:3px}
.heading{position:absolute;font-size:33px;letter-spacing:.3px;text-transform:uppercase;color:var(--ink);font-weight:300}
.heading b{font-weight:700;color:var(--gold)}

/* hero */
.hero{position:absolute;left:0;top:0;width:1200px;height:734px}
.hero-photo{position:absolute;inset:0;background:linear-gradient(180deg,#e4e4e4 0%,#d6d6d6 45%,#b9b9b9 70%,#dcdcdc 100%)}
.brand{position:absolute;left:100px;top:24px;display:flex;align-items:center;gap:8px;font-size:16px;font-weight:500;color:var(--gold);letter-spacing:1px;text-transform:uppercase}
.brand i{width:14px;height:14px;border-radius:50%;background:var(--gold);display:block}
.nav{position:absolute;left:277px;top:38px;display:flex;gap:31px;font-size:15px;color:#555}
.nav .active{color:var(--gold);font-weight:600}
.btn-join{left:816px;top:29px;width:177px;height:41px;font-size:12.5px}
.btn-login{position:absolute;left:1001px;top:29px;width:94px;height:41px;border:2px solid #666;border-radius:3px;display:flex;align-items:center;justify-content:center;font-weight:600;font-size:13px;color:#333;background:#f3f3f3}
.hero-dots{position:absolute;left:84px;top:337px;display:flex;flex-direction:column;gap:10px}
.hero-dots span{width:13px;height:13px;border:1.5px solid #777;border-radius:50%;display:block}
.hero-dots .on{background:var(--gold);border-color:var(--gold)}
.welcome{position:absolute;left:0;width:1200px;top:214px;text-align:center;font-size:15px;font-weight:500;color:#222;letter-spacing:.5px}
.hero-title{position:absolute;left:0;width:1200px;top:230px;text-align:center;font-size:45px;font-weight:700;color:var(--gold);letter-spacing:1px;text-transform:uppercase}
.hero-sub{position:absolute;left:0;width:1200px;top:290px;text-align:center;font-size:19px;line-height:28px;color:#333}
.search-tabs{position:absolute;left:284px;top:372px;display:flex;height:35px}
.search-tabs span{display:flex;align-items:center;justify-content:center;background:#fff;border:1px solid #bbb;font-size:12px;font-weight:600;color:#333;text-transform:uppercase}
.search-tabs .on{background:linear-gradient(180deg,var(--gold-light),var(--gold-dark));color:#fff;border-color:var(--gold)}
.search-filters{position:absolute;left:635px;top:372px;display:flex;gap:4px;height:35px}
.search-filters span{display:flex;align-items:center;gap:6px;padding:0 14px;background:#fff;border:1px solid #bbb;font-size:12px;font-weight:600;color:#333;text-transform:uppercase}
.search-box{position:absolute;left:284px;top:411px;width:633px;height:51px;background:#fff;border:1px solid #ccc;display:flex;align-items:center;gap:14px;padding-left:16px;font-size:13px;color:#777}
.btn-estimate{left:464px;top:475px;width:272px;height:39px;font-size:13px}
.category-bar{position:absolute;left:113px;top:705px;width:972px;height:49px;background:#fff;border:1.5px solid #999;border-radius:25px;display:flex;overflow:hidden}
.category-bar span{flex:1;display:flex;align-items:center;justify-content:center;font-size:13px;font-weight:600;color:#222;text-transform:uppercase;border-right:1px solid #ccc}
.category-bar span:last-child{border:none}
.category-bar .on{background:linear-gradient(180deg,var(--gold-light),var(--gold-dark));color:#fff}

/* about */
.about-accent{position:absolute;left:429px;top:1089px;width:187px;height:167px;background:linear-gradient(180deg,var(--gold-light),var(--gold-dark))}
.about-photo{position:absolute;left:113px;top:869px;width:481px;height:370px;background:linear-gradient(180deg,#2f3d5e 0%,#4a5670 40%,#5a6b4a 75%,#3e5a2a 100%)}
.about-text{position:absolute;left:660px;top:872px;width:430px}
.about-text h2{font-size:34px;font-weight:400;color:var(--ink);text-transform:uppercase;letter-spacing:.3px}
.about-text h3{margin-top:24px;font-size:16px;font-weight:600;color:var(--ink);line-height:25px}
.about-text p{margin-top:12px;font-size:13.5px;line-height:25px;color:var(--muted)}
.btn-about{left:660px;top:1163px;width:152px;height:41px}

/* sell / buy */
.split{position:absolute;top:1352px;height:380px;width:600px;display:flex;flex-direction:column;align-items:center;color:#fff}
.split-sell{left:0;background:linear-gradient(135deg,#3b2a12 0%,#1d1c1f 50%,#4a3416 100%)}
.split-buy{left:600px;background:linear-gradient(135deg,#b7860e 0%,#8a5e0a 50%,#5e3f08 100%)}
.split h2{margin-top:96px;font-size:31px;font-weight:700;text-transform:uppercase;letter-spacing:.5px}
.split p{margin-top:34px;font-size:16px;text-transform:uppercase}
.split .btn-outline{position:relative;margin-top:16px;width:198px;height:43px}

/* properties */
.properties{position:absolute;left:0;top:1732px;width:1200px;height:1034px;background:var(--cream)}
.title-rule{position:absolute;height:2px;width:70px;background:var(--gold)}
.prop-tabs{position:absolute;left:641px;top:95px;display:flex;align-items:center;gap:0;font-size:13px;font-weight:500;color:var(--ink)}
.prop-tabs span{height:43px;display:flex;align-items:center;padding:0 26px}
.prop-tabs .on{background:var(--gold);color:#fff;padding:0 14px;border-radius:2px}
.card{position:absolute;width:226px;height:317px;background:#fff;border-radius:6px;box-shadow:0 2px 8px rgba(0,0,0,.12);overflow:hidden;text-align:center}
.card .ph{height:164px;display:flex;align-items:center;justify-content:center}
.card .ph i{width:34px;height:34px;border-radius:50%;background:rgba(255,255,255,.35);border:1.5px solid #fff;display:block}
.card h4{margin-top:20px;font-size:13.5px;font-weight:600;color:var(--ink)}
.card .city{font-size:13px;color:#555;margin-top:2px}
.card .price{margin-top:12px;font-size:27px;font-weight:500;color:var(--ink)}
.card .feat{margin-top:10px;display:flex;justify-content:center;gap:12px;font-size:11px;color:#444}
.card .feat span{display:flex;align-items:center;gap:4px}
.btn-viewall{left:530px;top:888px;width:140px;height:43px}

/* featured listings */
.map{position:absolute;left:113px;top:2994px;width:972px;height:465px;border:6px solid var(--gold-dark);border-radius:8px;background:linear-gradient(135deg,#efe4cf 0%,#e9dcc0 55%,#d7e2c9 100%)}
.dropdown{position:absolute;left:754px;top:2893px;width:331px;height:44px;border:1.5px solid var(--gold);border-radius:3px;display:flex;align-items:center;justify-content:space-between;padding:0 14px 0 28px;font-size:13px;font-weight:600;color:var(--ink);text-transform:uppercase;background:#fff}

/* concierge */
.concierge{position:absolute;left:0;top:3650px;width:1200px;height:380px;background:linear-gradient(180deg,#a97811 0%,#c6951a 50%,#9a6a0e 100%);text-align:center;color:#fff}
.concierge h2{margin-top:72px;font-size:32px;font-weight:300;text-transform:uppercase}
.concierge h2 b{font-weight:700}
.band-text{margin:26px auto 0;width:770px;font-size:13.5px;line-height:25px}
.concierge .btn-outline{position:relative;margin:36px auto 0;width:238px;height:45px}

/* newsletter */
.news-title{position:absolute;left:0;width:1200px;top:4124px;text-align:center;font-size:33px;font-weight:300;color:#555;text-transform:uppercase}
.news-title b{font-weight:700;color:var(--gold)}
.news-q{position:absolute;left:0;width:1200px;top:4208px;text-align:center;font-size:15px;font-weight:500;color:var(--ink)}
.field{position:absolute;top:4266px;height:41px;border:1px solid #ccc;display:flex;align-items:center;padding-left:18px;font-size:13px;font-weight:500;color:#333;text-transform:uppercase;background:#fff}
.btn-submit{left:902px;top:4266px;width:132px;height:41px}
.consent{position:absolute;left:255px;top:4334px;width:760px;font-size:13px;line-height:24px;color:#444}
.consent i{display:inline-block;width:12px;height:12px;border:1px solid #555;margin-right:6px;vertical-align:-1px}

/* work with us */
.work{position:absolute;left:0;top:4484px;width:1200px;height:401px;background:linear-gradient(180deg,#1b2233 0%,#2a3143 60%,#1a1f2b 100%);text-align:center;color:#fff}
.work h2{margin-top:88px;font-size:32px;font-weight:300;text-transform:uppercase}
.work h2 b{font-weight:700;color:var(--gold-light)}
.work .band-text{margin-top:24px;width:770px}
.btn-work{position:relative;margin:32px auto 0;width:187px;height:45px}

/* footer */
.footer-brand{position:absolute;left:150px;top:5035px;display:flex;align-items:center;gap:8px;font-size:15px;font-weight:500;color:var(--gold);letter-spacing:1px;text-transform:uppercase}
.footer-brand i{width:14px;height:14px;border-radius:50%;background:var(--gold);display:block}
.social{position:absolute;top:5109px;width:36px;height:36px;border-radius:50%;border:1.5px solid #bbb;background:#fff}
.social.on{background:var(--gold);border-color:var(--gold)}
.f-col{position:absolute;top:4965px}
.f-col h5{font-size:18px;font-weight:600;color:var(--ink)}
.f-col .rule{width:70px;height:2px;background:var(--gold);margin-top:8px}
.f-col ul{list-style:none;margin-top:18px}
.f-col li{font-size:12.5px;color:#444;height:26px}
.contact-item{position:absolute;left:820px;display:flex;gap:14px;align-items:flex-start}
.contact-item .ic{width:28px;height:28px;border-radius:50%;border:1.5px solid var(--gold);display:flex;align-items:center;justify-content:center;flex:none}
.contact-item small{display:block;font-size:10px;color:#888}
.contact-item strong{display:block;font-size:12.5px;font-weight:600;color:var(--ink);line-height:16px}
.footer-bottom{position:absolute;top:5245px;font-size:12px;color:#555}
</style>
</head>
<body>

<header class="hero">
  <div class="hero-photo" role="img" aria-label="Bright living room with grey sofa, cushions, coffee table, rug and potted bonsai"></div>
  <div class="brand"><i></i>Agent Horvex</div>
  <nav class="nav">
    <span class="active">Home</span><span>Buy</span><span>Sell</span><span>Lease</span><span>Sold</span><span>Agents</span><span>Concierge</span>
  </nav>
  <div class="btn-gold btn-join">Join Agent Horvex</div>
  <div class="btn-login">LOGIN</div>
  <div class="hero-dots"><span></span><span class="on"></span><span></span><span></span></div>
  <div class="welcome">WELCOME TO</div>
  <h1 class="hero-title">Agent Horvex</h1>
  <p class="hero-sub">Australia's trusted real estate partner — Buy, sell, lease, or invest<br>with confidence across all states.</p>
  <div class="search-tabs">
    <span class="on" style="width:136px">Sell</span><span style="width:70px">Buy</span><span style="width:68px">Rent</span>
  </div>
  <div class="search-filters">
    <span>Min-Max Price</span>
    <span>Property Type
      <svg width="10" height="7" viewBox="0 0 10 7"><path d="M1 1l4 4 4-4" fill="none" stroke="#333" stroke-width="1.6"/></svg>
    </span>
  </div>
  <div class="search-box">
    <svg width="20" height="20" viewBox="0 0 20 20"><circle cx="8" cy="8" r="6" fill="none" stroke="#222" stroke-width="2"/><path d="M12.5 12.5l5.5 5.5" stroke="#222" stroke-width="2.2"/></svg>
    Search by City, Suburb, State
  </div>
  <div class="btn-gold btn-estimate">Get Instant Property Estimate</div>
  <div class="category-bar">
    <span>Rent</span><span class="on">Sell</span><span>Lease</span><span>Sold</span><span>Agents</span>
  </div>
</header>

<section aria-label="About us">
  <div class="about-accent"></div>
  <div class="about-photo" role="img" aria-label="Two-storey family home at dusk with lit windows, stone path and lawn"></div>
  <div class="about-text">
    <h2>About Us</h2>
    <h3>Gaerspiciatis unde omse snis iste natus error sseit voluptatem accusanti.</h3>
    <p>Gaerspiciatis unde omnis iste natus error sseit voluptatem accusantium doloremque laudan seftium, tsetam aseeem aperiam, eaque ipsa quae ab illo inventore veritatis et quasi architecto beatae vitae dicta sunt explicabo. Nemo enim ipsam voluptatem quia voluptas sit aspernatur.</p>
  </div>
  <div class="btn-gold btn-about">Learn More</div>
</section>

<section aria-label="Selling and buying">
  <div class="split split-sell" role="img" aria-label="Agent handing keys to clients outside a home at dusk">
    <h2>Selling a Home?</h2>
    <p>Discover your home's true value</p>
    <div class="btn-outline">Home Valuation</div>
  </div>
  <div class="split split-buy" role="img" aria-label="Agent meeting buyers in a bright interior, gold tinted">
    <h2>Buying a Home?</h2>
    <p>Explore available listings nearby</p>
    <div class="btn-outline" style="width:198px">Featured Properties</div>
  </div>
</section>

<section class="properties" aria-label="Properties this week">
  <h2 class="heading" style="left:110px;top:86px">Properties <b>this week.</b></h2>
  <div class="title-rule" style="left:110px;top:140px;background:#bbb"></div>
  <div class="prop-tabs"><span class="on">For Sale</span><span>For Rent</span><span>Open Times</span><span>Recent Sales</span></div>

  <!-- row 1 -->
  <article class="card" style="left:113px;top:183px"><div class="ph" role="img" aria-label="White two-storey house at dusk" style="background:linear-gradient(180deg,#4b5b82,#8a8f95 70%,#5c6b48)"></div><h4>1750 Ashcombe Avenue</h4><div class="city">Hollowbrook, NY 11743</div><div class="price">$500,000</div><div class="feat"><span><svg width="14" height="9"><rect x="0" y="3" width="14" height="4" fill="#333"/><rect x="0" y="0" width="3" height="9" fill="#333"/></svg>2 Bedrooms</span><span><svg width="11" height="10"><rect x="0" y="4" width="11" height="4" fill="#333"/><rect x="1" y="0" width="2" height="5" fill="#333"/></svg>2 Total Baths</span></div></article>
  <article class="card" style="left:362px;top:183px"><div class="ph" role="img" aria-label="Modern living room interior video tour" style="background:linear-gradient(180deg,#6b5240,#b49a82 60%,#8b7360)"><i></i></div><h4>1750 Ashcombe Avenue</h4><div class="city">Hollowbrook, NY 11743</div><div class="price">$500,000</div><div class="feat"><span><svg width="14" height="9"><rect x="0" y="3" width="14" height="4" fill="#333"/><rect x="0" y="0" width="3" height="9" fill="#333"/></svg>2 Bedrooms</span><span><svg width="11" height="10"><rect x="0" y="4" width="11" height="4" fill="#333"/><rect x="1" y="0" width="2" height="5" fill="#333"/></svg>2 Total Baths</span></div></article>
  <article class="card" style="left:610px;top:183px"><div class="ph" role="img" aria-label="Blue suburban house with white garage" style="background:linear-gradient(180deg,#9fb8d6,#4c5a74 55%,#6b8a4a)"></div><h4>1750 Ashcombe Avenue</h4><div class="city">Hollowbrook, NY 11743</div><div class="price">$500,000</div><div class="feat"><span><svg width="14" height="9"><rect x="0" y="3" width="14" height="4" fill="#333"/><rect x="0" y="0" width="3" height="9" fill="#333"/></svg>2 Bedrooms</span><span><svg width="11" height="10"><rect x="0" y="4" width="11" height="4" fill="#333"/><rect x="1" y="0" width="2" height="5" fill="#333"/></svg>2 Total Baths</span></div></article>
  <article class="card" style="left:857px;top:183px"><div class="ph" role="img" aria-label="Stone-fronted house with green lawn" style="background:linear-gradient(180deg,#7ba1d0,#6a6a70 50%,#5f9a3c)"></div><h4>1750 Ashcombe Avenue</h4><div class="city">Hollowbrook, NY 11743</div><div class="price">$500,000</div><div class="feat"><span><svg width="14" height="9"><rect x="0" y="3" width="14" height="4" fill="#333"/><rect x="0" y="0" width="3" height="9" fill="#333"/></svg>2 Bedrooms</span><span><svg width="11" height="10"><rect x="0" y="4" width="11" height="4" fill="#333"/><rect x="1" y="0" width="2" height="5" fill="#333"/></svg>2 Total Baths</span></div></article>

  <!-- row 2 -->
  <article class="card" style="left:113px;top:528px"><div class="ph" role="img" aria-label="White lounge with framed art and sofa" style="background:linear-gradient(180deg,#f1ece4,#d9d1c5 60%,#b9ae9f)"></div><h4>1750 Ashcombe Avenue</h4><div class="city">Hollowbrook, NY 11743</div><div class="price">$500,000</div><div class="feat"><span><svg width="14" height="9"><rect x="0" y="3" width="14" height="4" fill="#333"/><rect x="0" y="0" width="3" height="9" fill="#333"/></svg>2 Bedrooms</span><span><svg width="11" height="10"><rect x="0" y="4" width="11" height="4" fill="#333"/><rect x="1" y="0" width="2" height="5" fill="#333"/></svg>2 Total Baths</span></div></article>
  <article class="card" style="left:362px;top:528px"><div class="ph" role="img" aria-label="Home office with desk, chair and plants" style="background:linear-gradient(180deg,#9a8f7c,#c7bca8 50%,#7a5a3c)"></div><h4>1750 Ashcombe Avenue</h4><div class="city">Hollowbrook, NY 11743</div><div class="price">$500,000</div><div class="feat"><span><svg width="14" height="9"><rect x="0" y="3" width="14" height="4" fill="#333"/><rect x="0" y="0" width="3" height="9" fill="#333"/></svg>2 Bedrooms</span><span><svg width="11" height="10"><rect x="0" y="4" width="11" height="4" fill="#333"/><rect x="1" y="0" width="2" height="5" fill="#333"/></svg>2 Total Baths</span></div></article>
  <article class="card" style="left:610px;top:528px"><div class="ph" role="img" aria-label="Dark modern two-storey home video tour" style="background:linear-gradient(180deg,#5f7694,#3a3d44 55%,#6a5a48)"><i></i></div><h4>1750 Ashcombe Avenue</h4><div class="city">Hollowbrook, NY 11743</div><div class="price">$500,000</div><div class="feat"><span><svg width="14" height="9"><rect x="0" y="3" width="14" height="4" fill="#333"/><rect x="0" y="0" width="3" height="9" fill="#333"/></svg>2 Bedrooms</span><span><svg width="11" height="10"><rect x="0" y="4" width="11" height="4" fill="#333"/><rect x="1" y="0" width="2" height="5" fill="#333"/></svg>2 Total Baths</span></div></article>
  <article class="card" style="left:857px;top:528px"><div class="ph" role="img" aria-label="Open plan dining and living room video tour" style="background:linear-gradient(180deg,#4a4c52,#7a736a 55%,#3e3a36)"><i></i></div><h4>1750 Ashcombe Avenue</h4><div class="city">Hollowbrook, NY 11743</div><div class="price">$500,000</div><div class="feat"><span><svg width="14" height="9"><rect x="0" y="3" width="14" height="4" fill="#333"/><rect x="0" y="0" width="3" height="9" fill="#333"/></svg>2 Bedrooms</span><span><svg width="11" height="10"><rect x="0" y="4" width="11" height="4" fill="#333"/><rect x="1" y="0" width="2" height="5" fill="#333"/></svg>2 Total Baths</span></div></article>

  <div class="btn-gold btn-viewall">View All</div>
</section>

<section aria-label="Featured listings">
  <h2 class="heading" style="left:112px;top:2856px">Featured <b>Listings</b></h2>
  <div class="title-rule" style="left:112px;top:2910px;background:#bbb"></div>
  <p class="abs" style="left:113px;top:2929px;width:540px;font-size:15px;font-weight:500;line-height:26px;color:var(--ink)">Gaerspiciatis unde omse snis iste natus error sseit voluptatem accusanti.</p>
  <div class="dropdown">Queensland
    <svg width="14" height="9" viewBox="0 0 14 9"><path d="M1 1l6 6 6-6" fill="none" stroke="#333" stroke-width="2"/></svg>
  </div>
  <div class="map" role="img" aria-label="Map of central and northern Australia with listing location pins"></div>
  <div class="btn-gold" style="left:481px;top:3496px;width:238px;height:47px">View All Listings</div>
</section>

<section class="concierge" aria-label="Concierge" role="img" aria-label-detail="">
  <h2>Your personal <b>real estate concierge</b></h2>
  <p class="band-text">Gaerspiciatis unde omnis iste natus error sseit voluptatem accusantium doloremque laudan seftium, tsetam aseeem aperiam, eaque ipsa quae ab illo inventore veritatis et quasi architecto beatae vitae dicta sunt explicabo. Nemo enim ipsam voluptatem quia voluptas sit aspernatur.</p>
  <div class="btn-outline">Learn More</div>
</section>

<section aria-label="Newsletter">
  <h2 class="news-title">Receive exclusive <b>listings in your inbox</b></h2>
  <div class="title-rule" style="left:550px;top:4183px;background:#bbb;width:100px"></div>
  <p class="news-q">Are You Interested in Buying a Home?</p>
  <div class="field" style="left:197px;width:339px">Full Name</div>
  <div class="field" style="left:549px;width:341px">Email</div>
  <div class="btn-gold btn-submit">Submit</div>
  <p class="consent"><i></i>Gaerspiciatis unde omnis iste natus error sseit voluptatem accusantium doloremque laudan seftium, tsetam aseeem aperiam, eaque ipsa quae ab illo inventore veritatis et quasi architecto beatae vitae dicta sunt explicabo. Nemo enim ipsam voluptatem quia voluptas sit aspernatur.</p>
</section>

<section class="work" aria-label="Work with us">
  <h2>Work <b>with us</b></h2>
  <p class="band-text">Gaerspiciatis unde omnis iste natus error sseit voluptatem accusantium doloremque laudan seftium, tsetam aseeem aperiam, eaque ipsa quae ab illo inventore veritatis et quasi architecto beatae vitae dicta sunt explicabo. Nemo enim ipsam voluptatem quia voluptas sit aspernatur.</p>
  <div class="btn-gold btn-work" style="position:relative">Let's Connect</div>
</section>

<footer aria-label="Footer">
  <div class="footer-brand"><i></i>Agent Horvex</div>
  <span class="social" style="left:153px" aria-label="Social link"></span>
  <span class="social on" style="left:206px" aria-label="Social link"></span>
  <span class="social" style="left:261px" aria-label="Social link"></span>

  <div class="f-col" style="left:401px"><h5>Quick links</h5><div class="rule"></div>
    <ul><li>Home</li><li>Buy</li><li>Sell</li><li>Lease</li><li>Sold</li><li>Agents</li></ul></div>
  <div class="f-col" style="left:610px"><h5>Links</h5><div class="rule"></div>
    <ul><li>Copyright</li><li>Legal</li><li>Privacy</li><li>Accessibility</li><li>Concierge</li><li>Contact Us</li></ul></div>
  <div class="f-col" style="left:820px"><h5>Contact Us</h5><div class="rule"></div></div>

  <div class="contact-item" style="top:5024px"><span class="ic"><svg width="14" height="14" viewBox="0 0 14 14"><path d="M3 1l2.5 3-1.5 1.5a8 8 0 0 0 4.5 4.5L10 8.5l3 2.5-1.5 2A10 10 0 0 1 1 2.5z" fill="var(--gold)"/></svg></span><div><small>Call Us</small><strong>888.888.8888</strong></div></div>
  <div class="contact-item" style="top:5073px"><span class="ic"><svg width="14" height="11" viewBox="0 0 14 11"><rect x="0.5" y="0.5" width="13" height="10" fill="none" stroke="var(--gold)"/><path d="M1 1l6 5 6-5" fill="none" stroke="var(--gold)"/></svg></span><div><small>Email</small><strong>info@agenthorvex</strong></div></div>
  <div class="contact-item" style="top:5122px"><span class="ic"><svg width="12" height="15" viewBox="0 0 12 15"><path d="M6 14S1 8.5 1 5.5a5 5 0 0 1 10 0C11 8.5 6 14 6 14z" fill="var(--gold)"/><circle cx="6" cy="5.5" r="1.8" fill="#fff"/></svg></span><div style="width:230px"><small>Address</small><strong>Shop 2147B, Level 1 Coralgate Plaza Shopping Centre, 87 Tidewell Crescent, Southport</strong></div></div>

  <svg class="abs" style="left:1145px;top:5188px" width="16" height="44" viewBox="0 0 16 44"><path d="M8 44V3M2 9l6-7 6 7" fill="none" stroke="var(--gold)" stroke-width="2"/></svg>
  <div class="footer-bottom" style="left:111px">© 2025. All rights reserved.</div>
  <div class="footer-bottom" style="left:895px">Terms of use</div>
  <div class="footer-bottom" style="left:1005px">Privacy Policy</div>
</footer>

</body>
</html>
```